Welding Fabrication and Inspection Business Card Design

Welding Fabrication and Inspection Services,

Business

Industrial Machinery ServicesMohammed Rahim30 Ballarat Street, Carrow Heights East.4178.QLD

```html
<!DOCTYPE html>
<html lang="en">
<head>
<meta charset="utf-8">
<title>Corvane Plant Services – Business Card</title>
<link href="https://fonts.googleapis.com/css2?family=Lato:wght@400;700&display=swap" rel="stylesheet">
<style>
  :root {
    --backdrop: #e9e7e4;
    --card: #ffffff;
    --ink: #1c1c1c;
    --stripe: #3a3a3d;
    --accent: #8c1c1f;
    --muted: #3d3d3d;
    --tool-red: #8e2a2e;
    --tool-dark: #2a2a2a;
  }
  * { box-sizing: border-box; margin: 0; padding: 0; }
  html, body {
    width: 1200px; height: 913px; overflow: hidden;
    background: var(--backdrop);
    font-family: "Lato", sans-serif;
  }
  .canvas { position: relative; width: 1200px; height: 913px; }
  .card {
    position: absolute; width: 520px; height: 300px;
    background: var(--card);
    box-shadow: 0 6px 18px rgba(0,0,0,0.18);
    overflow: hidden;
  }
  .card--back { left: 70px; top: 120px; }
  .card--front { left: 610px; top: 480px; }

  .card__stripes { position: absolute; left: 0; right: 0; bottom: 0; height: 34px; }
  .card__stripe-wide { position: absolute; left: 0; right: 0; bottom: 10px; height: 12px; background: var(--stripe); }
  .card__stripe-thin { position: absolute; left: 0; right: 0; bottom: 0; height: 6px; background: var(--stripe); }

  .brand {
    display: flex; align-items: center; gap: 8px;
    color: var(--ink); font-weight: 700; font-size: 17px; letter-spacing: 0.2px;
  }
  .brand__mark { width: 10px; height: 10px; background: var(--ink); }

  .card--back .brand { position: absolute; left: 0; right: 0; top: 128px; justify-content: center; font-size: 20px; }

  .card--front .brand { position: absolute; left: 40px; top: 92px; }

  .product-photo {
    position: absolute; right: 34px; top: 26px; width: 112px; height: 58px;
    background: linear-gradient(135deg, var(--tool-red) 0%, #6d1f22 55%, var(--tool-dark) 100%);
    border-radius: 4px;
  }

  .contact { position: absolute; left: 40px; top: 196px; }
  .contact__name {
    color: var(--accent); font-weight: 400; font-size: 19px;
    text-transform: uppercase; letter-spacing: 0.6px; margin-bottom: 4px;
  }
  .contact__line { color: var(--muted); font-size: 13px; line-height: 1.35; }
</style>
</head>
<body>
<main class="canvas">
  <section class="card card--back" aria-label="Card back">
    <div class="brand"><span class="brand__mark"></span>Corvane Plant Services</div>
    <div class="card__stripes"><div class="card__stripe-wide"></div><div class="card__stripe-thin"></div></div>
  </section>

  <section class="card card--front" aria-label="Card front">
    <div class="product-photo" role="img" aria-label="Photo of a red handheld welding inspection tool with black cable"></div>
    <div class="brand"><span class="brand__mark"></span>Corvane Plant Services</div>
    <div class="contact">
      <p class="contact__name">Tariq Osmani</p>
      <p class="contact__line">17 Windorah Street, Carrow Heights East.</p>
      <p class="contact__line">4178.QLD</p>
    </div>
    <div class="card__stripes"><div class="card__stripe-wide"></div><div class="card__stripe-thin"></div></div>
  </section>
</main>
</body>
</html>
```